Private Optometric Practice Needs new Presentation Folders/Stationary

We recently moved our office and are looking to refresh our presentation folders and stationary. I tend to prefer simple, clean designs. We are a full scope optometric practice provide high quality eyewear, custom contact lenses, along with emergency care and treatment for dry eyes. We communicate with a lot of other doctors and want to exude professionalism. I have attached 2 versions of our logo.

Target Market(s)

Familys

Industry/Entity Type

Eyecare

Font styles to use
Sans Serif

Colors
0054AA
0677BA
7BADD7
CADEEF
E8F1F8

Requirements
Nice to have
• Bifold, areas to put information about practice, welcome letter

```html
<!DOCTYPE html>
<html lang="en">
<head>
<meta charset="utf-8">
<title>Lumen Vision – Stationery Suite</title>
<link rel="stylesheet" href="https://fonts.googleapis.com/css2?family=Lato:wght@300;400;700&family=Open+Sans:wght@400&family=Satisfy&display=swap">
<style>
  :root{
    --navy:#0c1a2c;
    --navy-2:#13263d;
    --blue:#35a4dd;
    --blue-deep:#0677ba;
    --ice:#e8f1f8;
    --paper:#ffffff;
    --ink:#4a4d52;
    --bg-cards:#3a3d42;
    --bg-folder:#8b8e90;
    --bg-letter:#4a4b4e;
    --bg-envelope:#333335;
    --heading:#ffffff;
  }
  *{box-sizing:border-box;margin:0;padding:0}
  html,body{width:1200px;height:1200px;overflow:hidden}
  body{font-family:'Lato',sans-serif;color:var(--ink)}
  .board{position:relative;width:1200px;height:1200px;display:grid;grid-template-columns:600px 600px;grid-template-rows:600px 600px}
  .quadrant{position:relative;overflow:hidden}
  .q-cards{background:var(--bg-cards)}
  .q-folder{background:var(--bg-folder)}
  .q-letter{background:var(--bg-letter)}
  .q-envelope{background:var(--bg-envelope)}
  .section-title{position:absolute;top:22px;left:0;width:100%;text-align:center;font-family:'Open Sans',sans-serif;font-weight:400;font-size:21px;letter-spacing:3px;color:var(--heading)}

  /* brand wordmark */
  .brand{font-family:'Lato',sans-serif;font-weight:300;text-align:center;line-height:1}
  .brand .brand-dot{display:block;margin:0 auto 8px;border-radius:50%;background:var(--blue)}
  .brand .brand-name{display:block;letter-spacing:.28em}
  .brand .brand-sub{display:block;letter-spacing:.32em}

  /* business cards */
  .card{position:absolute;width:300px;height:171px;box-shadow:0 6px 18px rgba(0,0,0,.35)}
  .card-front{left:150px;top:105px;background:var(--navy)}
  .card-front .tab{position:absolute;background:var(--blue)}
  .card-front .tab-top{left:14px;top:0;width:34px;height:40px}
  .card-front .tab-bottom{right:14px;bottom:0;width:34px;height:40px}
  .card-front .brand{position:absolute;left:0;right:0;top:44px;color:#fff}
  .card-front .brand-dot{width:22px;height:22px}
  .card-front .brand-name{font-size:22px}
  .card-front .brand-sub{font-size:10px;margin-top:6px;font-weight:700}
  .card-back{left:150px;top:320px;background:var(--paper);display:flex}
  .card-back .brand-side{width:118px;background:linear-gradient(135deg,#f3f3f3,#e4e5e6);display:flex;align-items:center;justify-content:center}
  .card-back .brand{color:var(--ink)}
  .card-back .brand-dot{width:20px;height:20px}
  .card-back .brand-name{font-size:14px}
  .card-back .brand-sub{font-size:8px;margin-top:5px;font-weight:700}
  .card-back .info-side{flex:1;background:var(--blue);color:#fff;padding:16px 14px}
  .person-first{font-size:12px;font-weight:300;letter-spacing:1px}
  .person-last{font-size:13px;font-weight:700;letter-spacing:.5px;padding-bottom:6px;border-bottom:1px solid #fff;margin-bottom:7px}
  .contact-list{list-style:none;font-size:9px;line-height:1.45}
  .contact-list li{display:flex;align-items:center;gap:5px}
  .contact-list svg{width:8px;height:8px;flex:none}
  .card-back .address{font-size:9px;margin-top:8px;padding-top:6px;border-top:1px solid #fff;line-height:1.4}

  /* presentation folder */
  .folder{position:absolute;left:80px;top:110px;width:440px}
  .folder-spread{display:flex;height:300px;box-shadow:0 8px 20px rgba(0,0,0,.3)}
  .folder-cover{position:relative;width:220px;background:linear-gradient(160deg,var(--navy-2),var(--navy))}
  .folder-cover .brand{position:absolute;left:0;right:0;top:110px;color:#fff}
  .folder-cover .brand-dot{width:18px;height:18px}
  .folder-cover .brand-name{font-size:15px}
  .folder-cover .brand-sub{font-size:7px;margin-top:5px;font-weight:700}
  .folder-cover .cover-contact{position:absolute;left:0;right:0;bottom:24px;text-align:center;color:#cfd8e2;font-size:6px;line-height:1.5}
  .folder-cover .stripe{position:absolute;left:0;right:0;bottom:8px;height:4px;background:var(--blue)}
  .folder-inside{position:relative;width:220px;background:linear-gradient(135deg,#fafafa,#ececed)}
  .folder-inside .brand{position:absolute;left:0;right:0;top:16px;color:var(--ink)}
  .folder-inside .brand-dot{width:12px;height:12px;margin-bottom:5px}
  .folder-inside .brand-name{font-size:10px}
  .folder-inside .brand-sub{font-size:5px;margin-top:3px;font-weight:700}
  .tagline{position:absolute;left:18px;top:86px;color:var(--ink);font-weight:300;font-size:15px;line-height:1}
  .tagline .tag-script{display:block;font-family:'Satisfy',cursive;color:var(--blue-deep);font-size:19px;margin-left:22px;margin-top:2px}
  .artwork-area{position:absolute;left:0;right:0;top:150px;bottom:0;background:linear-gradient(135deg,var(--blue) 0%,var(--blue-deep) 45%,var(--navy) 100%)}
  .folder-pockets{display:flex;gap:8px;height:80px}
  .pocket{position:relative;flex:1;background:var(--blue);border-radius:0 0 6px 6px}
  .pocket svg{position:absolute;left:0;top:0;width:100%;height:100%}
  .pocket .brand{position:absolute;left:0;right:0;top:26px;color:rgba(255,255,255,.45)}
  .pocket .brand-name{font-size:14px}

  /* letterhead */
  .letterhead{position:absolute;left:107px;top:658px;width:376px;height:486px;background:var(--paper)}
  .logo-block{position:absolute;display:flex;align-items:center;justify-content:center;background:linear-gradient(135deg,#f2f2f2,#e6e6e7);border-right:4px solid var(--blue)}
  .letterhead .logo-block{left:0;top:12px;width:96px;height:52px}
  .letterhead .brand-dot{width:14px;height:14px;margin-bottom:5px}
  .letterhead .brand-name{font-size:11px}
  .letterhead .brand-sub{font-size:7px;margin-top:2px;font-weight:700}
  .letter-contact{position:absolute;right:22px;top:19px;list-style:none;font-size:8px;line-height:1.25;color:var(--ink)}
  .letter-contact li{display:flex;align-items:center;gap:4px}
  .letter-contact svg{width:7px;height:7px;flex:none}
  .letter-edge{position:absolute;right:0;top:12px;width:13px;height:52px;background:var(--blue)}
  .faint-mark{position:absolute;font-family:'Lato',sans-serif;font-weight:300;letter-spacing:.2em;color:var(--ice);white-space:nowrap}
  .letterhead .faint-mark{left:0;right:0;top:226px;text-align:center;font-size:30px}
  .letter-footer{position:absolute;left:0;right:0;bottom:10px;height:16px;background:var(--blue);color:#fff;font-size:7.5px;display:flex;align-items:center;justify-content:center}

  /* envelope */
  .envelope{position:absolute;left:658px;top:780px;width:484px;height:242px;background:var(--paper);overflow:hidden}
  .envelope .logo-block{left:0;top:11px;width:117px;height:64px}
  .envelope .brand-dot{width:18px;height:18px;margin-bottom:6px}
  .envelope .brand-name{font-size:13px}
  .envelope .brand-sub{font-size:8px;margin-top:3px;font-weight:700}
  .return-address{position:absolute;left:17px;top:82px;font-size:9px;line-height:1.2;color:var(--ink)}
  .envelope .faint-mark{right:14px;top:98px;font-size:40px}
  .envelope-url{position:absolute;left:0;bottom:7px;width:152px;height:19px;background:var(--blue);color:#fff;font-size:8px;display:flex;align-items:center;justify-content:center}
</style>
</head>
<body>
<main class="board">

  <section class="quadrant q-cards">
    <h2 class="section-title">BUSINESS CARD DESIGN</h2>
    <article class="card card-front">
      <span class="tab tab-top"></span>
      <span class="tab tab-bottom"></span>
      <div class="brand"><span class="brand-dot"></span><span class="brand-name">LUMEN</span><span class="brand-sub">VISION</span></div>
    </article>
    <article class="card card-back">
      <div class="brand-side">
        <div class="brand"><span class="brand-dot"></span><span class="brand-name">LUMEN</span><span class="brand-sub">VISION</span></div>
      </div>
      <div class="info-side">
        <p class="person-first">DANIEL</p>
        <p class="person-last">WHITFORD, O.D.</p>
        <ul class="contact-list">
          <li><svg viewBox="0 0 10 10"><rect x="2.5" y="0.5" width="5" height="9" rx="1" fill="none" stroke="#fff"/></svg>(555) 014-2231</li>
          <li><svg viewBox="0 0 10 10"><rect x="1" y="4" width="8" height="5" fill="#fff"/><rect x="2.5" y="1" width="5" height="3" fill="none" stroke="#fff"/></svg>(555) 014-2298</li>
          <li><svg viewBox="0 0 10 10"><rect x="0.5" y="2" width="9" height="6" fill="none" stroke="#fff"/><path d="M0.5 2 L5 6 L9.5 2" fill="none" stroke="#fff"/></svg>dan@lumenvisioncare.com</li>
          <li><svg viewBox="0 0 10 10"><circle cx="5" cy="5" r="4.3" fill="none" stroke="#fff"/><path d="M0.7 5 H9.3 M5 0.7 V9.3" stroke="#fff"/></svg>www.lumenvisioncare.com</li>
        </ul>
        <p class="address">1420 Maple Grove Ave. Suite B<br>Fairview, OH 44126</p>
      </div>
    </article>
  </section>

  <section class="quadrant q-folder">
    <h2 class="section-title">PRESENTATION FOLDER DESIGN</h2>
    <div class="folder">
      <div class="folder-spread">
        <div class="folder-cover">
          <div class="brand"><span class="brand-dot"></span><span class="brand-name">LUMEN</span><span class="brand-sub">VISION</span></div>
          <p class="cover-contact">(555) 014-2231 · (555) 014-2298<br>dan@lumenvisioncare.com · www.lumenvisioncare.com<br>1420 Maple Grove Ave. Suite B, Fairview, OH 44126</p>
          <span class="stripe"></span>
        </div>
        <div class="folder-inside">
          <div class="brand"><span class="brand-dot"></span><span class="brand-name">LUMEN</span><span class="brand-sub">VISION</span></div>
          <p class="tagline">Eyesight is<span class="tag-script">Precious</span></p>
          <div class="artwork-area" role="img" aria-label="Geometric triangle artwork in blue and navy"></div>
        </div>
      </div>
      <div class="folder-pockets">
        <div class="pocket">
          <svg viewBox="0 0 216 80" aria-hidden="true" fill="none" stroke="var(--navy)" stroke-width="1">
            <path d="M70 22 L62 30 L70 38"/><path d="M146 22 L154 30 L146 38"/>
          </svg>
        </div>
        <div class="pocket">
          <div class="brand"><span class="brand-name">LUMEN</span></div>
        </div>
      </div>
    </div>
  </section>

  <section class="quadrant q-letter">
    <h2 class="section-title" style="top:20px">LETTERHEAD DESIGN</h2>
  </section>

  <section class="quadrant q-envelope">
    <h2 class="section-title" style="top:20px">ENVELOPE DESIGN</h2>
  </section>

  <article class="letterhead">
    <div class="logo-block">
      <div class="brand"><span class="brand-dot"></span><span class="brand-name">LUMEN</span><span class="brand-sub">VISION</span></div>
    </div>
    <ul class="letter-contact">
      <li><svg viewBox="0 0 10 10"><rect x="2.5" y="0.5" width="5" height="9" rx="1" fill="none" stroke="var(--blue)"/></svg>(555) 014-2231</li>
      <li><svg viewBox="0 0 10 10"><rect x="1" y="4" width="8" height="5" fill="var(--blue)"/><rect x="2.5" y="1" width="5" height="3" fill="none" stroke="var(--blue)"/></svg>(555) 014-2298</li>
      <li><svg viewBox="0 0 10 10"><rect x="0.5" y="2" width="9" height="6" fill="none" stroke="var(--blue)"/><path d="M0.5 2 L5 6 L9.5 2" fill="none" stroke="var(--blue)"/></svg>dan@lumenvisioncare.com</li>
      <li><svg viewBox="0 0 10 10"><circle cx="5" cy="5" r="4.3" fill="none" stroke="var(--blue)"/><path d="M0.7 5 H9.3 M5 0.7 V9.3" stroke="var(--blue)"/></svg>www.lumenvisioncare.com</li>
    </ul>
    <span class="letter-edge"></span>
    <p class="faint-mark">LUMEN</p>
    <footer class="letter-footer">1420 Maple Grove Ave. Suite B, Fairview, OH 44126</footer>
  </article>

  <article class="envelope">
    <div class="logo-block">
      <div class="brand"><span class="brand-dot"></span><span class="brand-name">LUMEN</span><span class="brand-sub">VISION</span></div>
    </div>
    <p class="return-address">1420 Maple Grove<br>Ave. Suite B, Fairview,<br>OH 44126</p>
    <p class="faint-mark">LUMEN</p>
    <div class="envelope-url">www.lumenvisioncare.com</div>
  </article>

</main>
</body>
</html>
```